Newsletter template

I am looking for 2 newsletter templates. My website is in Wordpress and I want to use in mailchimp for lists.

One newsletter is for local clients of design remodeling firm to be sent monthly

Second newsletter is for web store offerings to be sent weekly.

Target Market(s)

Luxury home and leisure

Industry/Entity Type

Store

Requirements
Must have
• Use logos and colors to seamlessly integrate with website,

```html
<!DOCTYPE html>
<html lang="en">
<head>
<meta charset="utf-8">
<title>Mara Linde Fine Living – Weekly Newsletter</title>
<link rel="stylesheet" href="https://fonts.googleapis.com/css2?family=Arvo:wght@400;700&family=Open+Sans:wght@400;600;700&display=swap">
<style>
  :root{
    --page:#ebebeb;
    --paper:#ffffff;
    --teal:#0ba6c3;
    --teal-text:#1a9fbc;
    --ink:#2b2b2b;
    --muted:#555;
    --yellow:#e3e81a;
    --yellow-ink:#3b3b1a;
    --frame:#e6e6e6;
  }
  *{box-sizing:border-box;margin:0;padding:0}
  html,body{width:722px;height:1200px;overflow:hidden}
  body{background:var(--page);font-family:"Open Sans",Arial,sans-serif;color:var(--ink);position:relative}
  .abs{position:absolute}
  .top-bar{font-size:7px;color:#555;top:21px}
  .top-bar.left{left:78px}
  .top-bar.right{right:75px}
  .top-bar a{color:var(--teal-text);text-decoration:none}
  .sheet{left:75px;top:38px;width:571px;height:1057px;background:var(--paper)}
  .brand{left:22px;top:12px;font-family:"Arvo",Georgia,serif;font-size:19px;color:var(--teal);line-height:1.1}
  .brand small{display:block;font-size:9px;letter-spacing:1px}
  .btn{background:var(--yellow);color:var(--yellow-ink);font-weight:700;text-align:center;text-transform:uppercase}
  .visit{left:465px;top:12px;width:91px;height:19px;font-size:7px;line-height:19px;box-shadow:0 1px 0 #b9bd10}
  .headline{left:26px;top:72px;font-family:"Arvo",Georgia,serif;line-height:1}
  .headline .l1{color:var(--teal);font-size:25px;display:block}
  .headline .l2{color:var(--ink);font-size:32px;display:block;margin-top:0}
  .today{left:31px;top:150px;font-family:"Arvo",Georgia,serif;font-size:14px}
  .arrows{left:503px;top:152px}
  .feature{left:0;top:180px;width:571px;height:229px;background:var(--teal)}
  .feature-photo{left:35px;top:40px;width:176px;height:170px;background:#fff;padding:6px;box-shadow:-4px 6px 8px rgba(0,0,0,.35)}
  .feature-photo div{width:100%;height:100%;background:linear-gradient(180deg,#fff 20%,#d99a45 40%,#c78636 60%,#fff 85%)}
  .feature-info{left:217px;top:20px;width:320px;color:#fff}
  .category{font-family:"Arvo",Georgia,serif;font-size:10px}
  .title{font-weight:700;font-size:11.5px;color:#1d2f33;margin-top:8px}
  .stock{font-size:8.5px;color:#1d3c44;margin-top:2px}
  .price-row{display:flex;align-items:center;margin-top:8px}
  .price{font-weight:700;font-size:19px;margin-right:18px}
  .buy{width:65px;height:21px;line-height:21px;font-size:9px;color:#fff}
  .details{font-size:7.2px;line-height:14.4px;color:#1a3d45;margin-top:10px}
  .details b{display:block;font-size:7.5px}
  .section-title{left:47px;top:428px;font-family:"Arvo",Georgia,serif;font-size:11px;color:var(--teal-text)}
  .card{width:116px}
  .card .thumb{width:116px;height:105px;border:1px solid var(--frame)}
  .card .name{font-size:7px;font-weight:700;color:var(--teal-text);line-height:12px;margin-top:8px;padding-left:2px}
  .card .cost{font-size:10px;margin-top:1px;padding-left:2px}
  .card .add{width:61px;height:13px;line-height:13px;font-size:6.5px;margin-top:4px;margin-left:2px}
  .pager{left:329px;top:1036px;display:flex;align-items:center;gap:5px}
  .pager span{width:14px;height:14px;border:1px solid #bbb;background:#fff;font-size:5.5px;line-height:12px;text-align:center;color:#333}
  .pager .on{background:#333;color:#fff;border-color:#333}
  .pager .gap{border:none;background:none;width:14px}
  .social-title{left:0;width:722px;top:1108px;text-align:center;font-family:"Arvo",Georgia,serif;font-size:11px;color:var(--teal-text)}
  .social-note{left:0;width:722px;top:1126px;text-align:center;font-size:7px;color:#444}
  .social-icons{left:300px;top:1145px;display:flex;gap:9px}
  .social-icons span{width:15px;height:15px;border-radius:50%;background:#111}
  .footer{left:0;width:722px;top:1179px;text-align:center;font-size:7px;color:#555;word-spacing:2px}
</style>
</head>
<body>
  <div class="abs top-bar left">Add to Wishlist &nbsp;|&nbsp; Add to Compare &nbsp;|&nbsp; Email to a Friend</div>
  <div class="abs top-bar right">Hello! Welcome to our shop. <a href="#">Check our current offers</a></div>

  <main class="abs sheet">
    <div class="abs brand">Mara Linde<small>FINE LIVING</small></div>
    <div class="abs btn visit">Visit our website</div>

    <h1 class="abs headline"><span class="l1">Our weekly newsletter of</span><span class="l2">our latest products</span></h1>

    <div class="abs today">Todays’s product</div>
    <svg class="abs arrows" width="20" height="12" viewBox="0 0 20 12"><path d="M7 1 2 6l5 5M13 1l5 5-5 5" fill="none" stroke="#333" stroke-width="2"/></svg>

    <section class="abs feature">
      <div class="abs feature-photo"><div role="img" aria-label="Teak shower bench product photo"></div></div>
      <div class="abs feature-info">
        <div class="category">BATH AND SPA</div>
        <div class="title">24 INCH ASIA TEAK SHOWER BENCH</div>
        <div class="stock">In stock Be the first to review this product</div>
        <div class="price-row"><span class="price">$169.95</span><span class="btn buy">BUY NOW</span></div>
        <p class="details"><b>Details:</b>This extended profile makes it ideal as a shower bench, but also extends its versatility as a small accent bench, or for use indoors or outdoors as part of your decor. Its minimalist Asian aesthetics will complement either a traditional or contemporary design flair. Use it for practicality to sit on, or as an accent piece with to hold your works of art. Its extended size also makes it ideal for use in locker rooms, spas, or gyms to add a touch of class to your spa decor.</p>
      </div>
    </section>

    <h2 class="abs section-title">Other Products You May Like</h2>

    <!-- row 1 -->
    <div class="abs card" style="left:47px;top:454px"><div class="thumb" role="img" aria-label="White towel bar photo" style="background:linear-gradient(135deg,#eee,#d8d8d8)"></div><div class="name">Asian Teak Bistro Counter<br>Height Stool</div><div class="cost">$ 200.00</div><div class="btn add">Add to cart</div></div>
    <div class="abs card" style="left:167px;top:454px"><div class="thumb" role="img" aria-label="Barbecue tool set photo" style="background:radial-gradient(circle,#444 35%,#fff 60%)"></div><div class="name">Asian Teak Bistro Counter<br>Height Stool</div><div class="cost">$ 200.00</div><div class="btn add">Add to cart</div></div>
    <div class="abs card" style="left:288px;top:454px"><div class="thumb" role="img" aria-label="Cutting board with knives photo" style="background:linear-gradient(180deg,#fff 35%,#d4a15a 55%,#fff 85%)"></div><div class="name">Asian Teak Bistro Counter<br>Height Stool</div><div class="cost">$ 200.00</div><div class="btn add">Add to cart</div></div>
    <div class="abs card" style="left:409px;top:454px"><div class="thumb" role="img" aria-label="Round serving board photo" style="background:radial-gradient(ellipse,#e4cf9e 40%,#fff 62%)"></div><div class="name">Asian Teak Bistro Counter<br>Height Stool</div><div class="cost">$ 200.00</div><div class="btn add">Add to cart</div></div>

    <!-- row 2 -->
    <div class="abs card" style="left:47px;top:644px"><div class="thumb" role="img" aria-label="Blue and white dinnerware photo" style="background:radial-gradient(ellipse,#8e9cc4 30%,#fff 65%)"></div><div class="name">Asian Teak Bistro Counter<br>Height Stool</div><div class="cost">$ 200.00</div><div class="btn add">Add to cart</div></div>
    <div class="abs card" style="left:167px;top:644px"><div class="thumb" role="img" aria-label="Shower panel photo" style="background:linear-gradient(90deg,#fff 42%,#333 47%,#333 53%,#fff 58%)"></div><div class="name">Asian Teak Bistro Counter<br>Height Stool</div><div class="cost">$ 200.00</div><div class="btn add">Add to cart</div></div>
    <div class="abs card" style="left:288px;top:644px"><div class="thumb" role="img" aria-label="Teak bench photo" style="background:linear-gradient(180deg,#fff 20%,#d59a48 40%,#c98a3a 65%,#fff 85%)"></div><div class="name">Asian Teak Bistro Counter<br>Height Stool</div><div class="cost">$ 200.00</div><div class="btn add">Add to cart</div></div>
    <div class="abs card" style="left:409px;top:644px"><div class="thumb" role="img" aria-label="Towel on grab bar photo" style="background:linear-gradient(135deg,#a9855a,#d9cdb6 55%,#8d6d48)"></div><div class="name">Asian Teak Bistro Counter<br>Height Stool</div><div class="cost">$ 200.00</div><div class="btn add">Add to cart</div></div>

    <!-- row 3 -->
    <div class="abs card" style="left:47px;top:843px"><div class="thumb" role="img" aria-label="Stacked colourful towels photo" style="background:linear-gradient(90deg,#fff 8%,#d97d4a 25%,#a2b7c8 50%,#9cc48a 75%,#fff 92%)"></div><div class="name">Asian Teak Bistro Counter<br>Height Stool</div><div class="cost">$ 200.00</div><div class="btn add">Add to cart</div></div>
    <div class="abs card" style="left:167px;top:843px"><div class="thumb" role="img" aria-label="Teak corner shower shelf photo" style="background:radial-gradient(ellipse,#8a4e2a 35%,#fff 65%)"></div><div class="name">Asian Teak Bistro Counter<br>Height Stool</div><div class="cost">$ 200.00</div><div class="btn add">Add to cart</div></div>
    <div class="abs card" style="left:288px;top:843px"><div class="thumb" role="img" aria-label="Teak half-round bench photo" style="background:radial-gradient(ellipse,#7a4526 35%,#fff 65%)"></div><div class="name">Asian Teak Bistro Counter<br>Height Stool</div><div class="cost">$ 200.00</div><div class="btn add">Add to cart</div></div>
    <div class="abs card" style="left:409px;top:843px"><div class="thumb" role="img" aria-label="Teak shelving tower photo" style="background:linear-gradient(90deg,#fff 25%,#7b3f22 40%,#8c4a28 60%,#fff 75%)"></div><div class="name">Asian Teak Bistro Counter<br>Height Stool</div><div class="cost">$ 200.00</div><div class="btn add">Add to cart</div></div>

    <nav class="abs pager" aria-label="Pages">
      <span>&lsaquo;</span><span>1</span><span>2</span><span>3</span><span class="on">4</span><span>5</span><span class="gap">....</span><span>15</span><span>30</span><span>45</span><span>&rsaquo;</span>
    </nav>
  </main>

  <div class="abs social-title">Social Media</div>
  <div class="abs social-note">Check our social media links and follow us!</div>
  <div class="abs social-icons" aria-label="Social media links"><span></span><span></span><span></span><span></span><span></span></div>

  <footer class="abs footer">About Us &nbsp;|&nbsp; Customer Service &nbsp;|&nbsp; Privacy Policy &nbsp;|&nbsp; Site Map &nbsp;|&nbsp; Search Terms &nbsp;|&nbsp; Advanced Search &nbsp;|&nbsp; Contact Us</footer>
</body>
</html>
```